Business Cards for Veltrin Massage and Wellness

I worked with designers from Pixel Harbor to make a wonderful logo and now I would like to use it in a business card. I have an intimate but progressive small clinical massage practice with far infrared sauna therapy for detox, vitadraw for pre and post surgery healing and ashiatsu and sports massage. We do lots of different modalities and I would like each therapist to have the same business card with their names on them. I would like to express our professionalism and connection to health.

I am attaching my logo and would like that included in the design. I love blues and greens. I would like something clean but creative, professional yet personality. I love the font copperplate gothic or I suppose whatever matches the logo. I would like to have the following information on the front of the card...

1. Logo

2. Address: Marlow Pavilion
2867 Tesslin Rd
Richmond, Va 23228
3. Phone: 804 519-2076

4. www.veltrinmassageandwellness.example

5. name of therapist, CMT (for example purposes Corin Mathers, CMT)

6. Optional information for front of card....
Far Infrared Sauna, Neuromuscular Therapy, VitaDraw, Detox Program, Deep Tissue, Swedish, Ashiatsu, Craniosacral Therapy, Reiki, Sports Massage, Couples Massage, Hot Stones, Cold Stones, LED Light Therapy

back of card...

1. Appointment Date/Time

2. Please provide 24 hours notice of cancellations

3. a line or space for appointment times.

```html
<!DOCTYPE html>
<html lang="en">
<head>
<meta charset="utf-8">
<title>Veltrin Massage and Wellness – Business Card</title>
<link rel="stylesheet" href="https://fonts.googleapis.com/css2?family=Cinzel:wght@400;700&family=Tinos&display=swap">
<style>
  :root {
    --olive: #9fa152;
    --mint: #72cca6;
    --ink: #111111;
    --paper: #ffffff;
  }
  * { margin: 0; padding: 0; box-sizing: border-box; }
  html, body { width: 1200px; height: 734px; overflow: hidden; background: var(--paper); }
  .card { position: relative; width: 1200px; height: 734px; background: var(--paper); }
  .brand-mark { position: absolute; left: 0; top: 0; }
  .brand-name {
    position: absolute; left: 383px; top: 96px;
    font-family: "Cinzel", serif; font-weight: 400; color: var(--olive);
    line-height: 1;
  }
  .brand-name .primary { display: block; font-size: 112px; letter-spacing: 12px; }
  .brand-name .secondary { display: block; font-size: 38px; letter-spacing: 11px; margin-top: 8px; }
  .brand-rule {
    position: absolute; left: 386px; top: 273px; width: 694px; height: 2px;
    background: var(--olive);
  }
  .tagline {
    position: absolute; left: 386px; top: 280px; width: 694px;
    font-family: "Tinos", serif; font-size: 28px; color: var(--mint);
    white-space: nowrap;
  }
  .therapist {
    position: absolute; left: 0; width: 1212px; top: 388px; text-align: center;
    font-family: "Cinzel", serif; font-weight: 700; font-size: 25px;
    letter-spacing: 1.5px; color: var(--ink);
  }
  .contact, .services {
    position: absolute; left: 0; width: 1212px; text-align: center;
    font-family: "Tinos", serif; font-size: 17px; letter-spacing: 1.2px;
    text-transform: uppercase; line-height: 23px;
  }
  .contact { top: 472px; color: var(--mint); }
  .contact .divider { margin: 0 10px; }
  .services { top: 540px; color: var(--olive); line-height: 23.5px; }
</style>
</head>
<body>
  <main class="card">
    <svg class="brand-mark" width="380" height="420" viewBox="0 0 380 420" aria-hidden="true">
      <circle cx="214" cy="214" r="128" fill="var(--mint)"/>
    </svg>

    <h1 class="brand-name">
      <span class="primary">VELTRIN</span>
      <span class="secondary">Massage and Wellness</span>
    </h1>
    <div class="brand-rule"></div>
    <p class="tagline">Promoting Preventative Care And Post-surgery Healing</p>

    <p class="therapist">Corin Mathers, CMT</p>

    <address class="contact">
      Marlow Pavilion 2867 Tesslin Rd Richmond, VA 23228<br>
      Phone 804 519-2076<span class="divider">|</span>Website www.veltrinmassageandwellness.example
    </address>

    <p class="services">
      Far Infrared Sauna • Neuromuscular Therapy • VitaDraw • Detox Program<br>
      Deep Tissue Swedish • Ashiatsu • Craniosacral Therapy • Reiki • Sports Massage Couples<br>
      Massage • Hot Stones • Cold Stones • LED Light Therapy
    </p>
  </main>
</body>
</html>
```